Bestselling author requires book cover for sequel

I need a book cover design for a sequel to Sunburnt in Flip-Flops (see Bookvale.co.uk) that maintains a little bit of continuity with the original, humo(u)r, a SUBTLE element of 'British holidaymaker in Spain/Tenerife/sub-tropical island' and will work for both ebook and print.
The most important thing is that the book will stand out in a crowd.
Use the same title at the moment (Sunburnt in Flip-Flops: Diaries of a Beachfront Waiter), but this will change according to the design.

• Cover must have humour and some continuity with the first book, Sunburnt in Flip-Flops.
Bear in mind the continuity doesn't have to be in using the same or similar image, it could just be in the font used.
A lot of the designs so far are just alternative images of a British man abroad. I need something more 'subtle'/clever to suggest Brit abroad.
• References to the 'Diaries' bit of the title. It's a humorous travel narrative, not a sordid 'tell-all'.

```html
<!DOCTYPE html>
<html lang="en">
<head>
<meta charset="utf-8">
<title>Sunburnt in Flip-Flops: Diaries of a Beachfront Waiter</title>
<link rel="stylesheet" href="https://fonts.googleapis.com/css2?family=Bodoni+Moda:opsz,wght@6..96,700;6..96,800&display=swap">
<style>
  :root {
    --page: #ffffff;
    --wood-light: #c8622a;
    --wood-mid: #b0521f;
    --wood-dark: #8f3d16;
    --wood-seam: #3a2012;
    --print-white: #f6f6f2;
    --print-edge: #d9d9d4;
    --sky-deep: #1f3a8a;
    --sky-mid: #4f6fb8;
    --sky-pale: #b7c6e6;
    --panel-cyan: #00ffff;
    --title-red: #ff1414;
    --subtitle-navy: #2e3192;
    --author-white: #ffffff;
  }
  * { margin: 0; padding: 0; box-sizing: border-box; }
  html, body {
    width: 866px; height: 1200px; overflow: hidden;
    background: var(--page);
  }
  .cover { display: block; width: 866px; height: 1200px; }
  .cover text {
    font-family: "Bodoni Moda", "Didot", "Times New Roman", serif;
    text-transform: uppercase;
  }
  .book-title { fill: var(--title-red); font-weight: 800; }
  .book-title--main { font-size: 74px; }
  .book-title--second { font-size: 60px; }
  .book-subtitle { fill: var(--subtitle-navy); font-weight: 700; font-size: 31px; }
  .author-name { fill: var(--author-white); font-weight: 700; font-size: 29px; }
</style>
</head>
<body>
<svg class="cover" viewBox="0 0 866 1200" role="document" aria-label="Book cover: Sunburnt in Flip-Flops, Diaries of a Beachfront Waiter, by Dan Hartley">
  <defs>
    <linearGradient id="wood-grain" x1="0" y1="0" x2="1" y2="1">
      <stop offset="0" stop-color="var(--wood-light)"/>
      <stop offset="0.55" stop-color="var(--wood-mid)"/>
      <stop offset="1" stop-color="var(--wood-dark)"/>
    </linearGradient>
    <linearGradient id="holiday-sky" x1="0" y1="0" x2="0.7" y2="1">
      <stop offset="0" stop-color="var(--sky-deep)"/>
      <stop offset="0.6" stop-color="var(--sky-mid)"/>
      <stop offset="1" stop-color="var(--sky-pale)"/>
    </linearGradient>
  </defs>

  <g class="cover-artwork">
    <rect role="img" aria-label="Photograph of weathered orange wooden floorboards"
          x="16" y="12" width="834" height="554" fill="url(#wood-grain)"/>
    <g class="floorboard-seams" stroke="var(--wood-seam)" stroke-width="3" opacity="0.5">
      <line x1="470" y1="12" x2="462" y2="58"/>
      <line x1="405" y1="512" x2="398" y2="566"/>
      <line x1="832" y1="380" x2="826" y2="566"/>
    </g>
    <polygon class="instant-print" points="218,55 782,92 752,533 192,500"
             fill="var(--print-white)" stroke="var(--print-edge)" stroke-width="1"/>
    <polygon role="img" aria-label="Holiday snapshot of a bare tree silhouetted against a blue sky with a jet contrail"
             points="240,95 753,128 735,449 221,418" fill="url(#holiday-sky)"/>
  </g>

  <g class="title-panel">
    <rect x="14" y="566" width="834" height="616" fill="var(--panel-cyan)"/>
    <text class="book-title book-title--main" x="38" y="660"
          textLength="790" lengthAdjust="spacingAndGlyphs">Sunburnt in</text>
    <text class="book-title book-title--second" x="38" y="726"
          textLength="510" lengthAdjust="spacingAndGlyphs">Flip-Flops</text>
    <text class="book-subtitle" x="40" y="780"
          textLength="760" lengthAdjust="spacingAndGlyphs">Diaries of a Beachfront Waiter</text>
    <text class="author-name" x="437" y="1150" text-anchor="middle"
          textLength="260" lengthAdjust="spacingAndGlyphs">Dan Hartley</text>
  </g>
</svg>
</body>
</html>
```